Residential Fence Company needs a Flyer Design

We need a flyer design for a fence company called "Brovalent". We custom build Wood, Vinyl, and Aluminum fences for residential customers. The flyer will be a sales promotion offering $500 off for a new fence installation. Prospective customers can call for a FREE estimate

We would like to showcase pictures of the fences we install (attached). We would like to see color designs/themes that that compliment our logo (attached). Additional information to include:

Website: www.brovalentgates.example
Phone Number: (317) 555-0148
Address: 2813 W. Maplewick Ave. Indianapolis, IN 46299

```html
<!DOCTYPE html>
<html lang="en">
<head>
<meta charset="utf-8">
<title>Brovalent Fence Flyer</title>
<link href="https://fonts.googleapis.com/css2?family=Krona+One&family=Oswald:wght@500;600&family=Montserrat:wght@400;600;700&display=swap" rel="stylesheet">
<style>
  :root {
    --ink: #0a0a0b;
    --white: #ffffff;
    --red: #c42026;
    --navy: #2b3a6b;
    --sky-top: #1e7fc4;
    --sky-mid: #5fb1e3;
    --leaf: #3f6a3a;
    --grass: #4f8a3a;
    --backdrop: #e9e9e9;
  }
  * { margin: 0; padding: 0; box-sizing: border-box; }
  html, body { width: 920px; height: 1200px; overflow: hidden; background: var(--backdrop); }
  .flyer {
    position: absolute; left: 29px; top: 0;
    width: 862px; height: 1200px; overflow: hidden;
    background: var(--ink);
  }
  .hero-photo {
    position: absolute; left: 0; top: 0; width: 862px; height: 520px;
    background: linear-gradient(180deg, var(--sky-top) 0%, var(--sky-mid) 45%, #8fb7c9 62%, var(--leaf) 82%, var(--grass) 100%);
  }
  .shapes { position: absolute; left: 0; top: 0; width: 862px; height: 1200px; }
  .headline {
    position: absolute; left: 50px; top: 30px;
    font-family: "Krona One", sans-serif; font-size: 42px; line-height: 50px;
    letter-spacing: -0.5px;
  }
  .headline .dark { color: var(--ink); }
  .headline .light { color: var(--white); }
  .offer {
    position: absolute; left: 50px; top: 300px; width: 210px;
    font-family: "Oswald", sans-serif; font-weight: 500; color: var(--white);
    text-align: center; text-transform: uppercase;
  }
  .offer .lead { font-size: 32px; line-height: 38px; }
  .offer .amount { font-size: 86px; line-height: 92px; font-weight: 600; }
  .offer .detail { font-size: 30px; line-height: 36px; }
  .pitch {
    position: absolute; left: 50px; top: 626px;
    font-family: "Krona One", sans-serif; font-size: 42px; line-height: 52px; color: var(--white);
  }
  .pitch .accent { color: var(--red); }
  .pitch-sub {
    position: absolute; left: 50px; top: 724px;
    font-family: "Montserrat", sans-serif; font-weight: 700; font-size: 13.5px; color: var(--white);
  }
  .benefits {
    position: absolute; left: 50px; top: 764px; list-style: none;
    font-family: "Montserrat", sans-serif; font-size: 17px; color: var(--white);
  }
  .benefits li { display: flex; align-items: center; height: 26.2px; }
  .benefits svg { width: 14px; height: 14px; margin-right: 10px; flex: none; }
  .brand {
    position: absolute; left: 48px; top: 1090px;
    display: flex; align-items: center; gap: 10px;
    font-family: "Montserrat", sans-serif; font-weight: 700; font-size: 34px; color: var(--navy);
  }
  .brand .mark { width: 22px; height: 22px; background: var(--navy); }
  .contact {
    position: absolute; right: 48px; top: 1008px; text-align: right;
    font-family: "Montserrat", sans-serif; color: var(--white);
  }
  .contact .cta { font-weight: 600; font-size: 25px; line-height: 32px; }
  .contact .phone { font-family: "Oswald", sans-serif; font-weight: 500; font-size: 62px; line-height: 70px; }
  .contact .web { font-weight: 600; font-size: 16px; line-height: 22px; padding-bottom: 4px; border-bottom: 1px solid var(--white); display: inline-block; }
  .contact .address { font-weight: 600; font-size: 14.5px; line-height: 24px; margin-top: 4px; }
</style>
</head>
<body>
<main class="flyer">
  <div class="hero-photo" role="img" aria-label="Photo of a black aluminum fence against a blue sky with trees"></div>

  <svg class="shapes" viewBox="0 0 862 1200" aria-hidden="false">
    <defs>
      <linearGradient id="vinylTone" x1="0" y1="0" x2="0" y2="1">
        <stop offset="0" stop-color="#4c9ad8"/><stop offset="0.55" stop-color="#dfe6ec"/><stop offset="1" stop-color="#4f8e34"/>
      </linearGradient>
      <linearGradient id="woodTone" x1="0" y1="0" x2="0" y2="1">
        <stop offset="0" stop-color="#9aa7a0"/><stop offset="0.3" stop-color="#d98a45"/><stop offset="0.8" stop-color="#c06a2c"/><stop offset="1" stop-color="#5d7a36"/>
      </linearGradient>
      <linearGradient id="railTone" x1="0" y1="0" x2="0" y2="1">
        <stop offset="0" stop-color="#6fa8d8"/><stop offset="0.3" stop-color="#7cab45"/><stop offset="1" stop-color="#8c9a4a"/>
      </linearGradient>
    </defs>
    <polygon class="dark-field" points="0,497 862,283 862,1200 0,1200" fill="var(--ink)"/>
    <polygon class="offer-badge" points="155,248 260,310 260,538 155,597 50,538 50,310" fill="var(--red)"/>
    <g class="gallery" stroke="var(--white)" stroke-width="8" stroke-linejoin="round">
      <polygon points="554,459 811,406 776,559 497,647" fill="url(#vinylTone)" role="img" aria-label="Photo of a white vinyl privacy fence on a lawn"/>
      <polygon points="554,611 811,558 776,711 497,799" fill="url(#woodTone)" role="img" aria-label="Photo of a cedar wood picket fence"/>
      <polygon points="554,763 811,710 776,863 497,951" fill="url(#railTone)" role="img" aria-label="Photo of a white rail ranch fence across a field"/>
    </g>
    <polygon class="footer-light" points="0,1045 862,935 862,1200 0,1200" fill="var(--white)"/>
    <polygon class="footer-accent" points="411,994 862,935 862,1200 352,1200" fill="var(--red)"/>
  </svg>

  <h1 class="headline">
    <span class="dark">BUILDING</span><br>
    <span class="light">ON THE</span><br>
    <span class="dark">AMERICAN</span><br>
    <span class="light">DREAM</span>
  </h1>

  <div class="offer">
    <div class="lead">Offering</div>
    <div class="amount">$500</div>
    <div class="detail">Off for<br>a new fence<br>installation</div>
  </div>

  <h2 class="pitch">WE <span class="accent">BUILD</span><br>FENCE</h2>
  <p class="pitch-sub">and we would love to build your fence too!</p>

  <ul class="benefits">
    <li><svg viewBox="0 0 14 14"><circle cx="7" cy="7" r="5.6" fill="none" stroke="var(--red)" stroke-width="1.8"/><path d="M4.3 7.2l2 2 3.6-4" fill="none" stroke="var(--red)" stroke-width="1.8"/></svg>Free Estimate</li>
    <li><svg viewBox="0 0 14 14"><circle cx="7" cy="7" r="5.6" fill="none" stroke="var(--red)" stroke-width="1.8"/><path d="M4.3 7.2l2 2 3.6-4" fill="none" stroke="var(--red)" stroke-width="1.8"/></svg>Proffesional Installation</li>
    <li><svg viewBox="0 0 14 14"><circle cx="7" cy="7" r="5.6" fill="none" stroke="var(--red)" stroke-width="1.8"/><path d="M4.3 7.2l2 2 3.6-4" fill="none" stroke="var(--red)" stroke-width="1.8"/></svg>Concrete in Every Post</li>
    <li><svg viewBox="0 0 14 14"><circle cx="7" cy="7" r="5.6" fill="none" stroke="var(--red)" stroke-width="1.8"/><path d="M4.3 7.2l2 2 3.6-4" fill="none" stroke="var(--red)" stroke-width="1.8"/></svg>HOA Submission Assistance</li>
    <li><svg viewBox="0 0 14 14"><circle cx="7" cy="7" r="5.6" fill="none" stroke="var(--red)" stroke-width="1.8"/><path d="M4.3 7.2l2 2 3.6-4" fill="none" stroke="var(--red)" stroke-width="1.8"/></svg>Lifetime Workmanshop Warranty</li>
    <li><svg viewBox="0 0 14 14"><circle cx="7" cy="7" r="5.6" fill="none" stroke="var(--red)" stroke-width="1.8"/><path d="M4.3 7.2l2 2 3.6-4" fill="none" stroke="var(--red)" stroke-width="1.8"/></svg>Experienced Installation Teams</li>
    <li><svg viewBox="0 0 14 14"><circle cx="7" cy="7" r="5.6" fill="none" stroke="var(--red)" stroke-width="1.8"/><path d="M4.3 7.2l2 2 3.6-4" fill="none" stroke="var(--red)" stroke-width="1.8"/></svg>Quality Workmanship &amp; Materials</li>
    <li><svg viewBox="0 0 14 14"><circle cx="7" cy="7" r="5.6" fill="none" stroke="var(--red)" stroke-width="1.8"/><path d="M4.3 7.2l2 2 3.6-4" fill="none" stroke="var(--red)" stroke-width="1.8"/></svg>Free Gate Adjustments for Life</li>
  </ul>

  <div class="brand"><span class="mark"></span>Brovalent</div>

  <div class="contact">
    <div class="cta">Contact Us Now!</div>
    <div class="phone">(317) 555-0148</div>
    <div class="web">www.brovalentgates.example</div>
    <div class="address">2813 W. Maplewick Ave. Indianapolis, IN 46299</div>
  </div>
</main>
</body>
</html>
```